New Business Card Design Project

I have a logo I would like to use on the business card. I want something that will stand out and that will be remembered.

Target Market(s)

People who collect gems, minerals and crystals.

Contact Information for Business Card

email - tkstonefalcon@mailbrook.net
phone # 617-203-4958

Font styles to use
Serif
Sans Serif
Decorative

Colors

Designer to choose colors to be used in the design.

Requirements
Must have
• The logo...two to choose from.
Nice to have
• An eye catching and memorable way to draw in people who collect gems minerals and crystals.

```html
<!DOCTYPE html>
<html lang="en">
<head>
<meta charset="utf-8">
<title>Stone Falcon – Business Card</title>
<link rel="stylesheet" href="https://fonts.googleapis.com/css2?family=Raleway:wght@300;800&display=swap">
<style>
  :root {
    --page-bg: #f4f4f4;
    --card-black: #080a09;
    --logo-black: #000000;
    --text-white: #f2f2f2;
    --icon-blue: #2b45b8;
    --facet-pink: #f17fb5;
    --facet-mauve: #c77fbf;
    --facet-plum: #9a4f8e;
    --facet-brown: #4a2a14;
    --facet-amber: #fbb463;
    --facet-ice: #bfe9f1;
    --facet-cyan: #5cc3d9;
    --facet-orange: #f28a3c;
    --facet-red: #ea4f25;
  }
  html, body {
    margin: 0;
    width: 982px;
    height: 1200px;
    overflow: hidden;
    background: var(--page-bg);
  }
  .business-card {
    position: absolute;
    left: 41px;
    top: 351px;
    width: 900px;
    height: 498px;
    background: var(--card-black);
    overflow: hidden;
  }
  .facet-band {
    position: absolute;
    left: 0;
    top: 171px;
    width: 900px;
    height: 156px;
    background: linear-gradient(90deg,
      var(--facet-pink) 0%, var(--facet-mauve) 12%, var(--facet-plum) 22%,
      var(--facet-brown) 30%, var(--facet-amber) 38%, var(--facet-plum) 62%,
      var(--facet-ice) 70%, var(--facet-cyan) 76%, var(--facet-amber) 82%,
      var(--facet-orange) 88%, var(--facet-red) 93%, var(--facet-brown) 100%);
  }
  .brand-badge {
    position: absolute;
    left: 282px;
    top: 71px;
    width: 336px;
    height: 336px;
    border-radius: 50%;
    background: var(--logo-black);
    display: flex;
    align-items: center;
    justify-content: center;
  }
  .brand-name {
    font-family: "Raleway", sans-serif;
    font-weight: 800;
    font-size: 38px;
    letter-spacing: 1px;
    color: var(--text-white);
    text-transform: uppercase;
  }
  .contact-list {
    position: absolute;
    left: 212px;
    top: 366px;
    margin: 0;
    padding: 0;
    list-style: none;
  }
  .contact-item {
    display: flex;
    align-items: center;
    height: 39px;
    font-family: "Raleway", sans-serif;
    font-weight: 300;
    font-size: 27px;
    color: var(--text-white);
  }
  .contact-icon {
    width: 30px;
    height: 24px;
    margin-right: 40px;
    fill: var(--icon-blue);
  }
</style>
</head>
<body>
  <main class="business-card">
    <div class="facet-band" role="img" aria-label="Band of colourful faceted crystal shapes in pink, plum, brown, amber, cyan and orange"></div>
    <div class="brand-badge">
      <span class="brand-name">Stone Falcon</span>
    </div>
    <ul class="contact-list">
      <li class="contact-item">
        <svg class="contact-icon" viewBox="0 0 30 24" aria-hidden="true">
          <path d="M8 2c1.5-.8 2.6.2 3.3 1.6l1.4 2.8c.6 1.2.2 2.2-.9 2.9l-1 .6c.8 2.6 2.6 4.8 5 6.2l.9-.8c1-.8 2.1-.9 3 0l2.3 2.2c1 1 1 2.2-.1 3.1-1.6 1.3-3.7 1.7-6 .7C10.2 19.4 6.6 14.7 5.5 9.6 5 6.6 6.1 3.2 8 2z"/>
        </svg>
        617-203-4958
      </li>
      <li class="contact-item">
        <svg class="contact-icon" viewBox="0 0 30 24" aria-hidden="true">
          <path d="M1 3h28v18H1z M3 5.5v13.2l8.4-6.7z M27 5.5l-8.4 6.5 8.4 6.7z M4 4.8l11 8.6 11-8.6z M12.6 13l-8.2 6.4h21.2L17.4 13 15 14.9z" fill-rule="evenodd"/>
        </svg>
        tkstonefalcon@mailbrook.net
      </li>
    </ul>
  </main>
</body>
</html>
```